Looking for a high-end business card design for a construction company

We are looking to update our business card design. We are a post-frame construction company that builds custom buildings, commercial spaces, homes, and anything else. We have multiple people working here so we would need something we can easily customize the information for the specific person. We need a name, website, cell phone, office phone as well as social icons. Our colors are black, white, and grey/silver so I would love a black background or something that is more striking than just a traditional white business card. Looking for something that is very professional with a high-end look/feel. I have attached our logos, they can be silver, white, grey, or black.
Industry/Entity Type
Construction
Contact Information for Business Card
Business logo, Name, Cell phone, Office phone, website, social Icons
Colors
Designer to choose only greyscale colors for use in the design.
Look and feel

```html
<!DOCTYPE html>
<html lang="en">
<head>
<meta charset="utf-8">
<title>Kestrel Builders, Inc. – Business Card</title>
<link rel="stylesheet" href="https://fonts.googleapis.com/css2?family=Montserrat:ital,wght@0,400;0,600;0,700;1,400&display=swap">
<style>
  :root {
    --stage: #2b2b2b;
    --card: #1c1c1d;
    --ink: #f4f4f4;
    --ink-soft: #cfcfcf;
    --rule: #8a8a8a;
    --emboss: #4a4a4c;
    --icon: #ffffff;
  }
  * { box-sizing: border-box; margin: 0; padding: 0; }
  html, body {
    width: 1200px; height: 900px; overflow: hidden;
    background: var(--stage);
    font-family: "Montserrat", sans-serif;
    color: var(--ink);
  }
  .stage {
    width: 1200px; height: 900px;
    display: flex; flex-direction: column;
    align-items: center; justify-content: center; gap: 40px;
  }
  .card {
    width: 700px; height: 400px;
    background: var(--card);
    position: relative;
    box-shadow: 0 12px 30px rgba(0,0,0,0.45);
  }
  /* Front */
  .card-front .contact {
    position: absolute; left: 56px; top: 118px; width: 360px;
  }
  .person-name {
    font-weight: 600; font-size: 26px; letter-spacing: 0.5px;
    text-transform: uppercase; line-height: 1.1;
  }
  .person-title {
    font-weight: 400; font-size: 14px; color: var(--ink-soft);
    margin-top: 4px;
  }
  .rule {
    height: 1px; margin: 16px 0 18px;
    background: linear-gradient(90deg, var(--rule), rgba(138,138,138,0));
    width: 560px;
  }
  .details { display: flex; gap: 34px; }
  .detail-list { list-style: none; display: flex; flex-direction: column; gap: 10px; }
  .detail {
    display: flex; align-items: center; gap: 10px;
    font-size: 15px; white-space: nowrap;
  }
  .detail .ic { width: 14px; height: 14px; flex: none; }
  .detail-list.web { margin-top: 44px; font-style: italic; }
  .brand-name {
    position: absolute; right: 48px; top: 150px;
    text-align: right; font-weight: 700; color: var(--ink);
    text-transform: uppercase; line-height: 1;
  }
  .brand-name .line1 { display: block; font-size: 38px; letter-spacing: 3px; }
  .brand-name .line2 { display: block; font-size: 20px; letter-spacing: 3px; margin-top: 6px; }
  /* Back */
  .card-back .brand-name {
    right: auto; left: 50%; top: 120px; transform: translateX(-50%);
    text-align: center; color: var(--emboss);
  }
  .card-back .brand-name .line1 { font-size: 64px; letter-spacing: 6px; }
  .card-back .brand-name .line2 { font-size: 32px; letter-spacing: 6px; margin-top: 8px; }
  .social {
    position: absolute; left: 50%; bottom: 70px; transform: translateX(-50%);
    display: flex; gap: 12px; list-style: none;
  }
  .social li {
    width: 26px; height: 26px; border-radius: 50%; background: var(--icon);
  }
</style>
</head>
<body>
<main class="stage">
  <section class="card card-front" aria-label="Business card front">
    <div class="contact">
      <h1 class="person-name">Dana Whitlock</h1>
      <p class="person-title">Managing Director</p>
      <div class="rule"></div>
      <div class="details">
        <ul class="detail-list">
          <li class="detail">
            <svg class="ic" viewBox="0 0 16 16" aria-hidden="true"><path fill="#f4f4f4" d="M3.6 1.5l2.3 2.6-1.3 1.8c.9 2 2.5 3.6 4.5 4.5l1.8-1.3 2.6 2.3-1.3 2.1C7 13 3 9 1.5 2.8z"/></svg>
            800-555-0142
          </li>
          <li class="detail">
            <svg class="ic" viewBox="0 0 16 16" aria-hidden="true"><rect x="4" y="1" width="8" height="14" rx="1.5" fill="none" stroke="#f4f4f4" stroke-width="1.3"/><circle cx="8" cy="12.5" r=".9" fill="#f4f4f4"/></svg>
            248-555-0187
          </li>
        </ul>
        <ul class="detail-list web">
          <li class="detail">
            <svg class="ic" viewBox="0 0 16 16" aria-hidden="true"><rect x="1" y="3.5" width="14" height="9" fill="#f4f4f4"/><path d="M1 3.5l7 5 7-5" fill="none" stroke="#1c1c1d" stroke-width="1.2"/></svg>
            info@kestrelbuildersinc.com
          </li>
          <li class="detail">
            <svg class="ic" viewBox="0 0 16 16" aria-hidden="true"><circle cx="8" cy="8" r="6.5" fill="none" stroke="#f4f4f4" stroke-width="1.3"/><ellipse cx="8" cy="8" rx="2.8" ry="6.5" fill="none" stroke="#f4f4f4" stroke-width="1"/><path d="M1.5 8h13" stroke="#f4f4f4" stroke-width="1"/></svg>
            www.kestrelbuildersinc.com
          </li>
        </ul>
      </div>
    </div>
    <p class="brand-name"><span class="line1">Kestrel</span><span class="line2">Builders, Inc.</span></p>
  </section>

  <section class="card card-back" aria-label="Business card back">
    <p class="brand-name"><span class="line1">Kestrel</span><span class="line2">Builders, Inc.</span></p>
    <ul class="social" aria-label="Social media links">
      <li></li><li></li><li></li><li></li>
    </ul>
  </section>
</main>
</body>
</html>
```